Korvane Works Business cards

We require somebody to design business cards for our new business.

Target Market(s)

Mining, haulage and civil.

Industry/Entity Type

Auto electrician in mining industry

Contact Information for Business Card

ABN, business email address, mobile number.

Colors
00AB8E
00BBA5
67D7C9
C6EFE9
E9F9F6

Requirements
Must have
• Services I offer: Breakdowns, Field Service, A/C Systems, Machine rewires, mine site vehicle fit outs

```html
<!DOCTYPE html>
<html lang="en">
<head>
<meta charset="utf-8">
<title>Korvane Works — Business Cards</title>
<link rel="stylesheet" href="https://fonts.googleapis.com/css2?family=Exo+2:wght@500;600;700&display=swap">
<style>
  :root {
    --stage: #2b2b2b;
    --card: #141414;
    --teal: #5cc9c0;
    --teal-deep: #00bba5;
    --ink: #f2f2f2;
    --muted: #d9d9d9;
  }
  * { box-sizing: border-box; margin: 0; padding: 0; }
  html, body { width: 1200px; height: 875px; overflow: hidden; }
  body {
    background: var(--stage);
    font-family: "Exo 2", sans-serif;
    display: flex;
    flex-direction: column;
    align-items: center;
    justify-content: center;
    gap: 40px;
  }
  .card {
    position: relative;
    width: 620px;
    height: 354px;
    background: var(--card);
    border-radius: 18px;
    overflow: hidden;
  }

  /* Services side */
  .brand {
    position: absolute;
    display: flex;
    align-items: center;
    gap: 10px;
    color: var(--teal);
    font-weight: 700;
    text-transform: uppercase;
    letter-spacing: 0.02em;
  }
  .brand__mark { width: 14px; height: 14px; background: var(--teal); flex: none; }
  .card--services .brand { left: 46px; top: 160px; font-size: 26px; }
  .divider {
    position: absolute;
    left: 322px; top: 72px;
    width: 2px; height: 212px;
    background: var(--teal);
  }
  .services { position: absolute; left: 350px; top: 96px; }
  .services__title {
    color: var(--teal);
    font-weight: 700;
    font-size: 24px;
    letter-spacing: 0.02em;
    margin-bottom: 10px;
  }
  .services__list { list-style: none; }
  .services__list li {
    color: var(--ink);
    font-weight: 600;
    font-size: 17px;
    line-height: 28px;
    padding-left: 20px;
    position: relative;
  }
  .services__list li::before {
    content: "";
    position: absolute;
    left: 4px; top: 12px;
    width: 6px; height: 6px;
    border-radius: 50%;
    background: var(--teal);
  }

  /* Contact side */
  .card--contact .brand { right: 40px; top: 60px; font-size: 24px; }
  .person { position: absolute; left: 40px; top: 150px; }
  .person__name { color: var(--teal); font-weight: 700; font-size: 34px; line-height: 40px; }
  .person__role { color: var(--ink); font-weight: 600; font-size: 16px; }
  .rule {
    position: absolute;
    left: 40px; top: 224px;
    width: 410px; height: 2px;
    background: var(--teal);
  }
  .abn {
    position: absolute;
    left: 440px; top: 196px;
    width: 180px; height: 30px;
    background: var(--teal);
    clip-path: polygon(18px 0, 100% 0, 100% 100%, 0 100%);
    color: var(--card);
    font-weight: 700;
    font-size: 14px;
    line-height: 30px;
    padding-left: 28px;
  }
  .address {
    position: absolute;
    left: 460px; top: 240px;
    color: var(--ink);
    font-weight: 600;
    font-size: 14px;
    line-height: 19px;
  }
  .contacts { position: absolute; left: 40px; top: 244px; list-style: none; }
  .contacts li {
    display: flex;
    align-items: center;
    gap: 10px;
    color: var(--ink);
    font-weight: 600;
    font-size: 15px;
    line-height: 24px;
  }
  .contacts svg { width: 13px; height: 13px; fill: var(--teal); flex: none; }
</style>
</head>
<body>

<section class="card card--services">
  <div class="brand"><span class="brand__mark"></span>Korvane Works</div>
  <div class="divider"></div>
  <div class="services">
    <h2 class="services__title">OUR SERVICES</h2>
    <ul class="services__list">
      <li>Breakdowns</li>
      <li>Field Service</li>
      <li>A/C Systems</li>
      <li>Machine rewires</li>
      <li>Mine site vehicle fit outs</li>
    </ul>
  </div>
</section>

<section class="card card--contact">
  <div class="brand"><span class="brand__mark"></span>Korvane Works</div>
  <div class="person">
    <h1 class="person__name">Daniel Reyes</h1>
    <p class="person__role">Head contractor</p>
  </div>
  <div class="rule"></div>
  <div class="abn">ABN: 48 210 377 906</div>
  <p class="address">214 Ironbark Rd.<br>Millbrook, GA 30999</p>
  <ul class="contacts">
    <li>
      <svg viewBox="0 0 24 24" aria-hidden="true"><path d="M6.6 10.8a15.1 15.1 0 0 0 6.6 6.6l2.2-2.2c.3-.3.7-.4 1-.2 1.1.4 2.3.6 3.6.6.6 0 1 .4 1 1V20c0 .6-.4 1-1 1A17 17 0 0 1 3 4c0-.6.4-1 1-1h3.5c.6 0 1 .4 1 1 0 1.3.2 2.5.6 3.6.1.3 0 .7-.2 1z"/></svg>
      555-014-2290
    </li>
    <li>
      <svg viewBox="0 0 24 24" aria-hidden="true"><path d="M2 5h20v14H2z M2 5l10 7 10-7" /></svg>
      info@korvaneworks.com
    </li>
    <li>
      <svg viewBox="0 0 24 24" aria-hidden="true"><circle cx="12" cy="12" r="10"/></svg>
      www.korvaneworks.com
    </li>
  </ul>
</section>

</body>
</html>
```